Food Safety 1-California workers only

3.25" by 4.5" Black and White Magazine Ad
This ad is to train California workers only.
Workers will be trained on: Food Safety, FSMA (Food Safety Modernization Act), using equipment safety, food processing production skills, worker safety, supervisory skills, communication skills.
"FREE TRAINING", The company does the training or Keystone Learning will provide the training.
Training grants range from $100,000 to $400,000.
Companies must be in business for profit.
Companies must train 200 employees or more.
This program is for California workers only.
Incumbent or new-hires are eligible.

Target Market(s)

California food processors, farms, food packaging, food processors, companies under FSMA, food safety, food production who need to train employees.

Industry/Entity Type

Food Production

Font styles to use
Serif
Sans Serif

Colors

Designer to choose colors to be used in the design.

Requirements
Must have
• This is a 3.25 inch by 4.5 inch magazine ad. It must be black and white. No color.
• The deliverable must be in basic PhotoShop. The ad does not need to include any graphics and be text only if needed. If you have a black and white graphic that will show well.
• Look at www.KLGFoodSafety..com
• Use the text from "MEALBOX-Photoshop-052018" file as your starting point.
Nice to have
• A black and white graphic about food. See www.KLGFoodSafety.com
Should not have
• No color.

```html
<!DOCTYPE html>
<html lang="en">
<head>
<meta charset="utf-8">
<title>Free Training – Keystone Learning</title>
<link href="https://fonts.googleapis.com/css2?family=Bitter:wght@700;800&family=Montserrat:wght@400;600;700&display=swap" rel="stylesheet">
<style>
  :root {
    --ink: #161616;
    --paper: #ffffff;
    --stage: #ecebe8;
    --quote-grey: #bdbdbd;
    --art-light: #f4f4f4;
    --art-mid: #d9d9d9;
  }
  * { margin: 0; padding: 0; box-sizing: border-box; }
  html, body {
    width: 1118px; height: 1200px; overflow: hidden;
    background: var(--stage);
  }
  .ad {
    position: absolute; left: 136px; top: 21px;
    width: 845px; height: 1158px;
    background: var(--paper);
    overflow: hidden;
    color: var(--ink);
    font-family: "Montserrat", sans-serif;
  }
  .food-art {
    position: absolute; left: 345px; top: 14px; width: 485px; height: 730px;
    background: radial-gradient(ellipse at 60% 40%, var(--art-mid) 0%, var(--art-light) 55%, rgba(255,255,255,0) 78%);
  }
  .corner-band { position: absolute; right: 0; top: 0; width: 340px; height: 340px; }
  .corner-band__label {
    position: absolute; left: 610px; top: 70px; width: 240px;
    transform: rotate(45deg); transform-origin: center;
    color: var(--paper); font-weight: 700; font-size: 48px; line-height: 52px;
    text-align: center; letter-spacing: 1px;
  }
  .topics {
    position: absolute; left: 36px; top: 56px;
    list-style: none; font-size: 21px; line-height: 26px; letter-spacing: .5px;
  }
  .headline {
    position: absolute; left: 36px; top: 258px;
    font-family: "Bitter", serif; font-weight: 800; font-size: 61px; line-height: 85px;
  }
  .headline__line--first { padding-left: 142px; }
  .quote-mark {
    position: absolute; font-family: "Bitter", serif; font-weight: 800;
    font-size: 250px; line-height: 1; color: var(--quote-grey);
  }
  .quote-mark--open { left: 28px; top: 190px; }
  .quote-mark--close { left: 500px; top: 440px; }
  .qualify { position: absolute; left: 36px; top: 648px; }
  .qualify__title { font-weight: 700; font-size: 34px; letter-spacing: .5px; margin-bottom: 12px; }
  .qualify__list { list-style: none; font-size: 21.5px; line-height: 26.2px; }
  .qualify__list li { position: relative; padding-left: 40px; }
  .qualify__list li::before { content: "•"; position: absolute; left: 2px; }
  .contact {
    position: absolute; left: 13px; top: 918px; width: 818px; height: 232px;
    background: var(--ink); color: var(--paper); padding: 28px 23px;
  }
  .contact__title { font-weight: 700; font-size: 37px; letter-spacing: .5px; margin-bottom: 12px; }
  .contact__lines { font-size: 21.5px; line-height: 26.2px; letter-spacing: .3px; }
</style>
</head>
<body>
<main class="ad">
  <div class="food-art" role="img" aria-label="Black and white ink illustration of vegetables: leafy greens, mushrooms, citrus slice, artichoke, pea pods, cauliflower, beetroot and garlic"></div>

  <svg class="corner-band" viewBox="0 0 340 340" aria-hidden="true">
    <polygon points="0,0 340,0 340,340" fill="var(--ink)"/>
  </svg>
  <div class="corner-band__label">FREE<br>TRAINING</div>

  <ul class="topics">
    <li>FOOD SAFETY</li>
    <li>FSMA</li>
    <li>PRODUCTION SKILLS</li>
    <li>WORKER SAFETY</li>
  </ul>

  <span class="quote-mark quote-mark--open" aria-hidden="true">“</span>
  <h1 class="headline">
    <div class="headline__line--first">WE DO</div>
    <div>THE TRAINING</div>
    <div>&amp; THE STATE</div>
    <div>PAYS FOR IT!</div>
  </h1>
  <span class="quote-mark quote-mark--close" aria-hidden="true">”</span>

  <section class="qualify">
    <h2 class="qualify__title">HOW TO QUALIFY</h2>
    <ul class="qualify__list">
      <li>Train California Workers Only</li>
      <li>Trainees must earn $11/hour</li>
      <li>Full-time workers only</li>
      <li>Employees must attend at least 8 Hours of training</li>
      <li>You must train 200 or more employees</li>
      <li>Incumbent or New-Hire workers are eligible</li>
      <li>Seasonal workers are eligible</li>
    </ul>
  </section>

  <section class="contact">
    <h2 class="contact__title">CONTACT</h2>
    <div class="contact__lines">
      <div>DANIEL WHITFIELD</div>
      <div>Keystone Learning Company, Inc.</div>
      <div>2150 Harbor Crest Drive Suite 310 Irvine, CA 92614</div>
      <div>www.KLGCAL.com | www.KLGFoodSafety.com</div>
      <div>Email: Dan.Whitfield@KLGCAL.com | Phone: (949) 555-0142</div>
    </div>
  </section>
</main>
</body>
</html>
```